Business Card for Financial Asset Management Company

Now we are launching a new company based in Tokyo.
The company information is below;

Company Name: Caldera Stewardship

Operations: Financial assets management, Proposing forming portfolio of assets, Consulting service, and advising to enhance your company's financial health

Corporate Colour: Japan Blue or Navy like below
http://pages.art.velmoreu.edu/tkovan/images/Indigo/Aqua-Indigo-104.jpg

It's dark and deep, and will get to fit to our clients as our relationships last longer and longer.

Our images for this colour are "Japanese style" and "pride in our craftmanship" , and also "gentle".

Corporate Key Image: an order taker who is sincere, polite, but courageous

We don't have our logo yet so please feel free to put any symbol on your design.

Please do not hesitate about asking any questions.
Thank you :-)

Reason: We are still discussin on final decision. Thank you for your understanding.

```html
<!DOCTYPE html>
<html lang="en">
<head>
<meta charset="utf-8">
<title>Caldera Stewardship — Business Card</title>
<link rel="stylesheet" href="https://fonts.googleapis.com/css2?family=Exo+2:wght@300;400&display=swap">
<style>
  :root {
    --stage: #6a5f9c;
    --indigo-deep: #1f1a5c;
    --indigo: #2f2878;
    --indigo-light: #4a3f98;
    --band: #050505;
    --band-soft: #2c2c2c;
    --ink: #ffffff;
    --ink-muted: #d9d9e6;
  }
  * { margin: 0; padding: 0; box-sizing: border-box; }
  html, body {
    width: 1200px;
    height: 900px;
    overflow: hidden;
    background: var(--stage);
    font-family: "Exo 2", sans-serif;
    color: var(--ink);
  }
  .card {
    position: absolute;
    left: 180px;
    top: 210px;
    width: 840px;
    height: 480px;
    overflow: hidden;
    box-shadow: 0 18px 40px rgba(20, 14, 60, 0.45);
  }
  .card-field {
    position: absolute;
    inset: 0;
    background:
      linear-gradient(135deg, var(--indigo-light) 0%, var(--indigo) 45%, var(--indigo-deep) 100%);
  }
  .band {
    position: absolute;
    background: var(--band);
  }
  .band--top {
    right: 0;
    top: 58px;
    width: 250px;
    height: 34px;
  }
  .band--address {
    left: 310px;
    right: 0;
    top: 292px;
    height: 36px;
    display: flex;
    align-items: center;
    padding-left: 22px;
    font-size: 19px;
    font-weight: 300;
    color: var(--ink-muted);
  }
  .band--contact {
    left: 310px;
    right: 0;
    top: 338px;
    height: 92px;
    padding: 12px 22px;
    font-size: 20px;
    font-weight: 300;
    line-height: 1.3;
  }
  .company {
    position: absolute;
    left: 0;
    top: 292px;
    width: 300px;
    height: 150px;
    background: linear-gradient(90deg, var(--band) 0%, var(--band-soft) 70%, #444 100%);
    display: flex;
    flex-direction: column;
    justify-content: center;
    padding-left: 34px;
    font-size: 32px;
    font-weight: 300;
    line-height: 1.15;
    letter-spacing: 0.02em;
    text-transform: uppercase;
  }
  .holder {
    position: absolute;
    right: 70px;
    top: 118px;
    text-align: right;
  }
  .holder-name {
    font-size: 40px;
    font-weight: 300;
    letter-spacing: 0.01em;
  }
  .holder-role {
    display: inline-block;
    margin-top: 8px;
    background: var(--band);
    padding: 4px 18px;
    font-size: 17px;
    font-weight: 300;
    color: var(--ink-muted);
  }
</style>
</head>
<body>
  <article class="card">
    <div class="card-field" role="img" aria-label="Faceted indigo geometric background"></div>

    <div class="band band--top"></div>

    <div class="holder">
      <div class="holder-name">Mika Sorano</div>
      <div class="holder-role">Position</div>
    </div>

    <div class="band band--address">Address</div>

    <div class="band band--contact">
      <div class="contact-line">123 456 7890</div>
      <div class="contact-line">123 456 7891</div>
      <div class="contact-line">contact@calderastewardship.jp</div>
    </div>

    <div class="company">
      <span>Caldera</span>
      <span>Stewardship</span>
    </div>
  </article>
</body>
</html>
```